Picture Ads

We need some banner ads for our home business opportunity, we are evolving from text to picture ads. I have added some examples of what other distributors are using. We are looking for something really eye catching with some good key words and nice bright colours and to include our photo (attached)
Key words to include:
Booming online business
Personal Development and Leadership Industry
Earn an executive income from home
Simple 3 step system
Make up to $5,000 per sale
Not MLM
The size needs to be: 1000 x 35 pixels
13.9 x 4.75 Inches
35.3 x 11.1 cm
I think different platforms accept different sizes, not too familiar with it yet, any guidance welcome. I've clicked project for 2 days if that is to prioritise the order?
Many thanks,
Maren

Industry/Entity Type

Business

```html
<!DOCTYPE html>
<html lang="en">
<head>
<meta charset="utf-8">
<title>Booming Online Business Banner</title>
<link href="https://fonts.googleapis.com/css2?family=Alegreya:wght@500&family=Orbitron:wght@400;900&family=Didact+Gothic&display=swap" rel="stylesheet">
<style>
  :root {
    --blue-deep: #0f4f96;
    --blue-mid: #1b67b8;
    --blue-light: #3a86d0;
    --navy-band: rgba(8, 36, 74, 0.82);
    --yellow: #ffd400;
    --white: #ffffff;
    --text-soft: #e4eefa;
    --button-text: #1a2a3c;
    --tick-light: #7fdcff;
    --tick-dark: #0d6fa8;
  }
  html, body {
    margin: 0;
    padding: 0;
    width: 1200px;
    height: 402px;
    overflow: hidden;
  }
  .banner {
    position: relative;
    width: 1200px;
    height: 402px;
    overflow: hidden;
    background: linear-gradient(100deg, var(--blue-deep) 0%, var(--blue-mid) 45%, var(--blue-light) 100%);
    font-family: "Didact Gothic", sans-serif;
  }
  .swoosh {
    position: absolute;
    inset: 0;
  }
  .headline-band {
    position: absolute;
    left: 0;
    top: 43px;
    width: 884px;
    height: 73px;
    background: var(--navy-band);
  }
  .headline {
    position: absolute;
    left: 96px;
    top: 44px;
    margin: 0;
    height: 72px;
    display: flex;
    align-items: center;
    white-space: nowrap;
  }
  .headline-lead {
    font-family: "Alegreya", serif;
    font-weight: 500;
    font-size: 32px;
    letter-spacing: 1.5px;
    color: var(--white);
    margin-right: 14px;
    padding-top: 6px;
  }
  .headline-key {
    font-family: "Orbitron", sans-serif;
    font-weight: 900;
    font-size: 48px;
    letter-spacing: 3px;
    color: var(--yellow);
    text-shadow: 0 2px 3px rgba(0,0,0,0.45);
  }
  .subline {
    position: absolute;
    left: 98px;
    top: 156px;
    margin: 0;
    color: var(--text-soft);
    font-size: 22px;
    letter-spacing: 3px;
    line-height: 35px;
    text-transform: uppercase;
  }
  .cta {
    position: absolute;
    left: 96px;
    top: 250px;
    width: 256px;
    height: 49px;
    background: var(--white);
    display: flex;
    align-items: center;
    justify-content: center;
    font-family: "Orbitron", sans-serif;
    font-size: 17px;
    letter-spacing: 2.5px;
    color: var(--button-text);
    text-decoration: none;
  }
  .portrait {
    position: absolute;
    left: 918px;
    top: 46px;
    width: 272px;
    height: 256px;
    border-radius: 50%;
    background: radial-gradient(ellipse at 50% 50%, #6fb4ea 0%, #3f8ed6 50%, rgba(40,110,190,0.6) 72%, rgba(30,100,180,0) 100%);
  }
  .benefits-band {
    position: absolute;
    left: 0;
    top: 319px;
    width: 1200px;
    height: 83px;
    background: var(--navy-band);
  }
  .benefit {
    position: absolute;
    top: 340px;
    display: flex;
    align-items: center;
    color: var(--white);
    font-size: 21px;
    letter-spacing: 2px;
    text-transform: uppercase;
    white-space: nowrap;
  }
  .benefit svg { margin-right: 14px; }
  .benefit .amount {
    color: var(--yellow);
    font-weight: bold;
    margin: 0 7px;
  }
  .benefit-system { left: 80px; }
  .benefit-earnings { left: 465px; }
  .benefit-model { left: 934px; }
</style>
</head>
<body>
<div class="banner">
  <svg class="swoosh" width="1200" height="402" viewBox="0 0 1200 402" aria-hidden="true">
    <path d="M0 150 C 300 60, 700 40, 1200 130 L1200 110 C 700 20, 300 40, 0 120 Z" fill="#ffffff" opacity="0.06"/>
    <path d="M300 402 C 500 260, 800 200, 1200 220 L1200 250 C 820 240, 540 290, 360 402 Z" fill="#ffffff" opacity="0.07"/>
    <path d="M0 0 L260 0 C 180 60, 90 120, 0 160 Z" fill="#ffffff" opacity="0.05"/>
  </svg>

  <div class="headline-band"></div>
  <h1 class="headline">
    <span class="headline-lead">BOOMING ONLINE</span>
    <span class="headline-key">BUSINESS</span>
  </h1>

  <p class="subline">Earn an executive income from home<br>Personal development &amp; leadership industry</p>

  <a class="cta" href="#">LEARN MORE</a>

  <div class="portrait" role="img" aria-label="Photo of the two business owners smiling outdoors"></div>

  <div class="benefits-band"></div>

  <div class="benefit benefit-system">
    <svg width="31" height="31" viewBox="0 0 31 31" aria-hidden="true">
      <defs><radialGradient id="tickA" cx="40%" cy="35%" r="65%"><stop offset="0" stop-color="#7fdcff"/><stop offset="1" stop-color="#0d6fa8"/></radialGradient></defs>
      <circle cx="15.5" cy="15.5" r="14" fill="url(#tickA)" stroke="#cfefff" stroke-width="1.5"/>
      <path d="M8 15 L13.5 21 L23 8" fill="none" stroke="#ffffff" stroke-width="3.2" stroke-linecap="round" stroke-linejoin="round"/>
    </svg>
    Simple 3 step system
  </div>

  <div class="benefit benefit-earnings">
    <svg width="31" height="31" viewBox="0 0 31 31" aria-hidden="true">
      <circle cx="15.5" cy="15.5" r="14" fill="url(#tickA)" stroke="#cfefff" stroke-width="1.5"/>
      <path d="M8 15 L13.5 21 L23 8" fill="none" stroke="#ffffff" stroke-width="3.2" stroke-linecap="round" stroke-linejoin="round"/>
    </svg>
    Make up to<span class="amount">$5,000</span>per sale
  </div>

  <div class="benefit benefit-model">
    <svg width="31" height="31" viewBox="0 0 31 31" aria-hidden="true">
      <circle cx="15.5" cy="15.5" r="14" fill="url(#tickA)" stroke="#cfefff" stroke-width="1.5"/>
      <path d="M8 15 L13.5 21 L23 8" fill="none" stroke="#ffffff" stroke-width="3.2" stroke-linecap="round" stroke-linejoin="round"/>
    </svg>
    Not MLM
  </div>
</div>
</body>
</html>
```